Verdell Chiropractic, achieve your health goals, get better each day one step at a time

A mobile friendly site, fresh look, easy to navigate, has interface with pw/chirply, etc. Blog posts. Uses new logo. Content and address to current site is mirvaton.com. The current site will give you scope of project for content. The logo is not the final but close. Will upload final next week.
Convey the concept that heath is a process, it does not just happen. We take steps to achieve what we want in life including health.

Target Market(s)

30 to 70 year old. Needing health care

Industry/Entity Type

Health Care

Coding

Coded - Design and coding required

Number of Pages Required

5+ page

Font styles to use
Sans Serif

Colors

Designer to choose colors to be used in the design.

Requirements
Must have
• mobile friendly, easy to navigate, PW/Chirply interface, blog, room for current content
Nice to have
• potential for commerce, statistics
Should not have
• Same old look and feel as everything else out there

```html
<!DOCTYPE html>
<html lang="en">
<head>
<meta charset="utf-8">
<title>Verdell Chiropractic</title>
<link rel="stylesheet" href="https://fonts.googleapis.com/css2?family=Didact+Gothic&display=swap">
<style>
  :root {
    --blue: #2f7fbd;
    --blue-panel: #3388c6;
    --blue-text: #2d7ab8;
    --green: #a3cf7e;
    --ink: #4a4f55;
    --white: #ffffff;
    --card: rgba(255,255,255,0.85);
  }
  * { box-sizing: border-box; margin: 0; padding: 0; }
  html, body { width: 1152px; height: 1200px; overflow: hidden; background: var(--white); }
  body { font-family: "Didact Gothic", "Helvetica Neue", Arial, sans-serif; color: var(--ink); position: relative; }

  .site-header { position: absolute; left: 0; top: 0; width: 1152px; height: 74px; background: var(--white); box-shadow: 0 1px 4px rgba(0,0,0,0.06); z-index: 3; }
  .brand { position: absolute; left: 150px; top: 25px; display: flex; align-items: center; gap: 7px; color: var(--blue); font-size: 15px; }
  .brand-dot { width: 12px; height: 12px; border-radius: 50%; background: var(--blue); }
  .main-nav { position: absolute; top: 0; height: 66px; left: 0; right: 0; }
  .main-nav a { position: absolute; top: 26px; font-size: 11px; color: var(--ink); text-decoration: none; }
  .btn { display: flex; align-items: center; justify-content: center; background: var(--blue); color: var(--white); border-radius: 16px; text-decoration: none; }
  .main-nav .btn-appointment { position: absolute; left: 857px; top: 18px; width: 141px; height: 30px; font-size: 11px; color: var(--white); }

  .hero { position: absolute; left: 0; top: 74px; width: 1152px; height: 451px;
    background: linear-gradient(90deg, #3d86c2 0%, #6ea6cc 40%, #8fbcbd 70%, #a6cd8e 100%); }
  .hero-title { position: absolute; left: 445px; top: 198px; width: 500px; text-align: center; color: var(--white); font-size: 32px; line-height: 32px; font-weight: 400; letter-spacing: 0.5px; }

  .conditions-panel { position: absolute; left: 163px; top: 498px; width: 313px; height: 464px; border-radius: 6px;
    background: linear-gradient(180deg, #2f82c2, #3a8dc8 60%, #3488c5); z-index: 2; }
  .conditions-list { list-style: none; position: absolute; left: 0; top: 52px; width: 100%; }
  .conditions-list li { height: 36.8px; display: flex; align-items: center; justify-content: center; color: var(--white); font-size: 18px; }
  .conditions-list li.is-active span { background: var(--white); color: var(--blue-text); width: 170px; height: 37px; border-radius: 19px; display: flex; align-items: center; justify-content: center; }

  .condition-photo { position: absolute; left: 665px; top: 559px; width: 325px; height: 215px; border-radius: 13px;
    background: linear-gradient(120deg, #9cc26f, #c9a488 50%, #e7e6e0); }
  .condition-title { position: absolute; left: 509px; top: 795px; font-size: 24px; color: var(--blue-text); font-weight: 400; }
  .condition-text { position: absolute; left: 509px; top: 842px; width: 475px; font-size: 12px; line-height: 15.7px; }
  .btn-read { position: absolute; left: 509px; top: 924px; width: 105px; height: 26px; font-size: 11px; border-radius: 13px; }

  .services-band { position: absolute; left: 0; top: 1018px; width: 1152px; height: 182px;
    background: linear-gradient(90deg, #cfd6df, #e1e4e8 45%, #b5cde0 85%, #d4dde6); }
  .service-card { position: absolute; background: var(--card); display: flex; align-items: center; color: var(--blue-text); font-size: 16px; }
  .service-next { left: 0; top: 1074px; width: 442px; height: 83px; border-radius: 0 8px 8px 0; padding-left: 282px; }
  .service-next-2 { left: 0; top: 1192px; width: 442px; height: 20px; border-radius: 0 8px 0 0; }
  .service-prev { left: 709px; top: 1134px; width: 443px; height: 80px; border-radius: 8px 0 0 0; padding-left: 37px; align-items: flex-start; padding-top: 30px; }
  .arrow { margin: 0 16px; }
</style>
</head>
<body>
  <header class="site-header">
    <div class="brand"><span class="brand-dot"></span>Verdell Chiropractic</div>
    <nav class="main-nav">
      <a href="#" style="left:425px">Home</a>
      <a href="#" style="left:484px">Meet Dr. Marlow</a>
      <a href="#" style="left:580px">Testimonials</a>
      <a href="#" style="left:670px">Faqs</a>
      <a href="#" style="left:723px">Resources</a>
      <a href="#" style="left:804px">Contact</a>
      <a href="#" class="btn btn-appointment">Make an Appointment</a>
    </nav>
  </header>

  <section class="hero" role="img" aria-label="Doctor in blue scrubs with arms crossed in a clinic, blue-green overlay">
    <h1 class="hero-title">THE MOST VALUABLE<br>THING IS YOUR HEALTH</h1>
  </section>

  <aside class="conditions-panel" role="img" aria-label="Faint skeleton and spine illustration behind the list of conditions">
    <ul class="conditions-list">
      <li class="is-active"><span>Headaches</span></li>
      <li>Neck Pain</li>
      <li>Shoulder Pain</li>
      <li>Wrist Pain</li>
      <li>Lower Back</li>
      <li>Hip &amp; Leg Pain</li>
      <li>Knee Pain</li>
      <li>Heel Pain</li>
      <li>Fibromyalgia</li>
      <li>Disc Bulge</li>
    </ul>
  </aside>

  <div class="condition-photo" role="img" aria-label="Woman holding her temples with a headache"></div>
  <h2 class="condition-title">HEADACHES</h2>
  <p class="condition-text">Chronic headaches and migraines afflict many Americans.&nbsp; The often debilitating pain affects their families and jobs.&nbsp; The primary causes are structural (spinal nerves and muscles), chemical (hormones, allergies and blood sugar) and emotional (muscle tension and stress hormones).&nbsp; The most common approach to</p>
  <a href="#" class="btn btn-read">Read More</a>

  <section class="services-band" role="img" aria-label="Doctor at a desk with clipboard, laptop and stethoscope"></section>
  <a class="service-card service-next">Chiropractic<span class="arrow">&gt;</span></a>
  <div class="service-card service-next-2"></div>
  <a class="service-card service-prev"><span class="arrow" style="margin-left:0">&lt;</span>Other Services</a>
</body>
</html>
```